Business Card Design - Law Firm

We are a boutique law firm located near the beach in Manly, Australia. We have recently had a new logo designed and are revamping our business cards with the new logo.

We have recently had a business card design done for us but are not entirely happy with it. We are looking for something modern, simplistic but striking. We would like to see multiple designs.

We have attached a word document which includes our new logo and the current business card design which we are looking at moving away from.

We would like the business cards to be double sided. We would like the design to include something which we can print in gloss colour when we send it to the business card printers.

```html
<!DOCTYPE html>
<html lang="en">
<head>
<meta charset="utf-8">
<title>Harlow &amp; Partners – Business Cards</title>
<link rel="stylesheet" href="https://fonts.googleapis.com/css2?family=Lato:wght@400;700&family=Montserrat:wght@600;700&display=swap">
<style>
  :root {
    --backdrop: #2b2b2d;
    --card: #111113;
    --card-edge: #1a1a1d;
    --accent-blue: #5b68c9;
    --accent-gold: #c9a866;
    --text-light: #e9e9ec;
    --rule: #4a4a50;
  }
  * { box-sizing: border-box; margin: 0; padding: 0; }
  html, body {
    width: 1200px; height: 900px; overflow: hidden;
    background: var(--backdrop);
  }
  .stage {
    width: 1200px; height: 900px;
    display: flex; flex-direction: column; align-items: center; justify-content: center;
    gap: 48px;
  }
  .card {
    position: relative;
    width: 560px; height: 320px;
    background: linear-gradient(160deg, var(--card-edge), var(--card));
    box-shadow: 0 14px 30px rgba(0,0,0,.45);
    overflow: hidden;
  }
  .card__band {
    position: absolute; left: 0; right: 0; bottom: 0;
    height: 9px; background: var(--accent-blue);
  }
  /* Front */
  .card--front {
    display: flex; align-items: center; justify-content: center;
  }
  .brand {
    display: flex; align-items: center; gap: 14px;
  }
  .brand__dot {
    width: 18px; height: 18px; border-radius: 50%;
    background: var(--accent-blue);
  }
  .brand__name {
    font-family: "Montserrat", sans-serif;
    font-weight: 700; font-size: 28px; letter-spacing: .5px;
    color: var(--text-light);
  }
  /* Back */
  .card--back {
    display: flex; flex-direction: column; align-items: center;
    padding-top: 34px; text-align: center;
    font-family: "Lato", sans-serif; color: var(--text-light);
  }
  .person__name {
    font-family: "Montserrat", sans-serif; font-weight: 700;
    font-size: 22px; letter-spacing: .5px; color: var(--accent-blue);
  }
  .person__role {
    font-size: 15px; color: var(--accent-gold); margin-top: 2px;
  }
  .divider {
    width: 200px; height: 1px; background: var(--rule); margin: 8px 0;
  }
  .contact-icons { display: flex; gap: 5px; margin-bottom: 6px; }
  .contact-icons svg { width: 20px; height: 20px; display: block; }
  .contact__line { font-size: 15px; line-height: 1.25; }
  .office__name {
    font-family: "Lato", sans-serif; font-weight: 700;
    font-size: 15px; letter-spacing: .5px; color: var(--accent-blue);
  }
  .office__line { font-size: 15px; line-height: 1.25; }
</style>
</head>
<body>
<main class="stage">
  <section class="card card--front" aria-label="Card front">
    <div class="brand">
      <span class="brand__dot"></span>
      <span class="brand__name">Harlow &amp; Partners</span>
    </div>
    <div class="card__band"></div>
  </section>

  <section class="card card--back" aria-label="Card back">
    <h1 class="person__name">MAYA ELLISON</h1>
    <p class="person__role">Practice Manager</p>
    <div class="divider"></div>
    <div class="contact-icons">
      <svg viewBox="0 0 20 20" aria-label="Phone" role="img">
        <rect width="20" height="20" rx="4" fill="var(--accent-blue)"/>
        <path d="M6 5h3l1 3-2 1a7 7 0 0 0 3 3l1-2 3 1v3a1 1 0 0 1-1 1A10 10 0 0 1 5 6a1 1 0 0 1 1-1z" fill="var(--card)"/>
      </svg>
      <svg viewBox="0 0 20 20" aria-label="Fax" role="img">
        <rect width="20" height="20" rx="4" fill="var(--accent-blue)"/>
        <rect x="6.5" y="4" width="7" height="4" fill="var(--card)"/>
        <rect x="4" y="8.5" width="12" height="5" rx="1" fill="var(--card)"/>
        <rect x="6.5" y="12" width="7" height="4" fill="var(--card)"/>
      </svg>
      <svg viewBox="0 0 20 20" aria-label="Website" role="img">
        <rect width="20" height="20" rx="4" fill="var(--accent-blue)"/>
        <circle cx="10" cy="10" r="5.5" fill="none" stroke="var(--card)" stroke-width="1.5"/>
        <ellipse cx="10" cy="10" rx="2.3" ry="5.5" fill="none" stroke="var(--card)" stroke-width="1.2"/>
        <line x1="4.5" y1="10" x2="15.5" y2="10" stroke="var(--card)" stroke-width="1.2"/>
      </svg>
    </div>
    <p class="contact__line">(02) 9410 3187</p>
    <p class="contact__line">(02) 9410 3188</p>
    <p class="contact__line">www.harlowpartners.com.au</p>
    <div class="divider"></div>
    <p class="office__name">HARLOW &amp; PARTNERS</p>
    <p class="office__line">Suite 4, 18 Tidewater Lane</p>
    <p class="office__line">SEAVIEW&nbsp;&nbsp; NSW&nbsp;&nbsp; 2000</p>
    <div class="card__band"></div>
  </section>
</main>
</body>
</html>
```